Greek Souvlaki Restaurant Menu Design

We would like to redesign our menu (at the moment just a price-list without any graphics) and create something more fun.

You can find all the items we are offering at the following link / our e-shop:
https://olivebranchkitchen.example/orders/en/order/
I have also attached a printout of the above with hand written notes on the sections and items that will be included.

Our menu is divided to a couple of parts:
- Souvlaki Bar and Grill
- Authentic Greek Cuisine
- Wine List
- Desserts
- Bakaliko

This project will take on the first part of our menu, which is the Souvlaki Bar and Grill. If we are happy with your design, we will then develop the rest of our menu.

Souvlaki Bar and Grill
---------------------------

Our souvlaki can be customised to the customer requirements. The following links have similar set ups:

WOW!Patty
https://gr.pinboardly.example/pin/100000000000000001/
I like the way they have set it up, but the graphics and colours used are not my thing. I also like they way they have split up the steps, choose, top it of, etc.

The Krokk
https://gr.pinboardly.example/pin/100000000000000002/
I hate the step 1,2,3 on the left side. It does not make it playful. Like the fact that they have used pictures of the ingredients.

https://gr.pinboardly.example/pin/100000000000000003/
Hate the graphics, like the concept.

-------------

First Sections: Our Souvliaki Pita Wrap

The steps to customise a souvlaki can be found on the following link:
https://olivebranchkitchen.example/orders/en/order/ and choose pita wrap.

Most of the one side of our Souvliaki/Grill menu should be dedicated to our Pita Wraps.

It should have a small description of the Greek Souvlaki Pita Wrap. Something along the lines of "Get a whole meal all wrapped up with our delicious Greek Pita Wraps. Containing protein, sauce and salad". Improvements of this line are welcome.

It should then have the steps to customise it.

Step One.
Choose Base:
1. Chicken Skewer
2. Pork Skewer
3. etc
Price and options can be found on the above link on our website

Step Two.
Add one of our delicious home made sauces.
Options can be found on our website.

Step Three
Finalise it with the ingredients of your choice.
The customer can select multiple incredients

Step Four.
Feeling Hungry? Add extras:
Extras and Prices can be found on the link provided.

Buy two wraps and save. Takeaway only!
You will find this option as "Double Souvlaki Pita Wrap Offer."
Instead of 2x5.5 = £11 pay £10.5. This offer should also be mentioned somewhere on this section.

-----

Second Section - Our Platters

Skewers Platter and Gyros Platter

Options can be found by clicking on the items on the link provided.

Extras and Pita Bread option are common. Meat options are different and skewers have a choice of side. Meat options have 2/3 skewers and 200/300 grams of gyros, so they can probably be combined somehow.

These section can also be called Naked / Open Souvlaki Platters

Third Section
From Our Grill

All options from this section together with modifiers (can be see if you click on each item). I would like pictures from each item.

Forth Section
Meal Deals, starter combo and Set Menu.

Meal Deal for 1/2 and 4 are wraps with extras. The for 4 is not on the pdf and will be up on our website soon, so please check. I think those are easy to e incorporated next to the pita wrap section as upgrades to save.

Set menus are various items.

If they can fit on this page somehow we incorporate them, if not we can make a separate page with the offers / meals deals. If a separate page is created them the meal deal from our kitchen and vegetarean set menu should also be included.

Fifth Section
Salads and Starter

I would like all options from Hot and Cold starter and our salad. I would like pictures next to all options, if possible.

-----

Final notes/ideas.

Wraps, platters and grill could be one page front and back. Salads and starters could be a different page(s) or sections.

The menu should be easily updated and we would like a format where we can update prices and descriptions.

Prices and descriptions can be found on the link provided.

Feel free to improve our descriptions and titles. Please do mention where you made improvements, so we can approve them.

Our kitchen, dessert and wine menu will be given as a separate project and priority will be given to the person that won this competition.

If you need better quality pictures please let us know, most of the pictures we do have them in raw format too.

------

Some designs that I like. To give you an idea of the design I would like to see:

https://www.craftmarketly.example/listing/100000001/american-menu-restaurant-cafe-menus
I would love to see something like that for the grill/salad/starter side of our menu, since it has space for pictures.

https://gr.pinboardly.example/pin/100000000000000004/
I would love to see something like that, where the incredients of a souvlaki come together. This is optional and does not have to be there.

https://gr.pinboardly.example/pin/100000000000000005/

https://gr.pinboardly.example/pin/100000000000000006/

https://gr.pinboardly.example/pin/100000000000000007/

https://gr.pinboardly.example/pin/100000000000000008/

Target Market(s)

London

Font styles to use
Serif
Sans Serif

Colors
abd037
3277b5
33a6d7

Requirements
Must have
• Build your own souvlaki section. See description for examples.

Pictures for starters and salads.

Should be elegant
Nice to have
• Incorporate our relevant meal deals on the souvlaki pita section

```html
<!DOCTYPE html>
<html lang="en">
<head>
<meta charset="utf-8">
<title>Meraki Kitchen – Souvlaki Bar and Grill Menu</title>
<link rel="stylesheet" href="https://fonts.googleapis.com/css2?family=Fira+Sans:wght@300;400;500&family=Fira+Sans+Condensed:wght@400;500;700&family=Signika:wght@600;700&display=swap">
<style>
  :root {
    --brand-blue: #2e86b9;
    --title-blue: #2a7db2;
    --pattern-blue: #3a8fc2;
    --ink: #2b2b2b;
    --badge: #2a2a2a;
    --paper: #ffffff;
    --backdrop: #e9e9e9;
  }
  * { box-sizing: border-box; margin: 0; padding: 0; }
  html, body { width: 1200px; height: 822px; overflow: hidden; }
  body {
    background: var(--backdrop);
    font-family: "Fira Sans", Arial, sans-serif;
    color: var(--ink);
    position: relative;
  }
  .page {
    position: absolute;
    top: 95px;
    width: 450px;
    height: 634px;
    background: var(--paper);
    box-shadow: 0 4px 14px rgba(0,0,0,.18);
  }

  /* Cover */
  .cover { left: 100px; }
  .cover-band {
    position: absolute; top: 0; bottom: 0; width: 125px;
    background: var(--pattern-blue);
  }
  .cover-band--left { left: 0; }
  .cover-band--right { right: 0; }
  .cover-name {
    position: absolute; left: 125px; right: 125px; top: 300px;
    text-align: center; color: var(--title-blue);
    font-family: "Fira Sans Condensed", "Arial Narrow", sans-serif; font-weight: 400;
    font-size: 28px; line-height: 1; letter-spacing: 1px;
  }

  /* Menu page */
  .menu { left: 640px; }
  .menu-brand {
    position: absolute; left: 28px; top: 46px;
    font-family: "Fira Sans Condensed", "Arial Narrow", sans-serif; font-weight: 400;
    color: #333; font-size: 14px; line-height: 1;
  }
  .menu-title {
    position: absolute; right: 34px; top: 20px; text-align: right;
    font-family: "Signika", "Trebuchet MS", sans-serif; font-weight: 700;
    color: var(--title-blue); font-size: 30px; line-height: 1.12;
  }
  .rule { position: absolute; left: 144px; right: 34px; height: 1px; background: #777; }
  .photo { position: absolute; }
  .photo--wrap { left: 32px; top: 105px; width: 112px; height: 91px;
    background: linear-gradient(135deg, #4f86b3, #b99468 55%, #e6e1d8); }
  .photo--platter { left: 32px; top: 452px; width: 112px; height: 89px;
    background: linear-gradient(135deg, #7aa3c4, #d8b063 55%, #eef0f0); }
  .item-title {
    position: absolute; left: 150px;
    font-family: "Fira Sans", Arial, sans-serif; font-weight: 500;
    font-size: 16px; color: #222;
  }
  .item-title .price { color: var(--brand-blue); font-size: 14px; margin-left: 4px; font-weight: 500; }
  .item-title--platter { right: 34px; text-align: left; }
  .item-title--platter .price { float: right; }
  .intro {
    position: absolute; left: 162px; top: 143px; width: 134px;
    text-align: center; font-size: 9.5px; line-height: 1.3; font-weight: 300; color: #333;
  }
  .offer-badge {
    position: absolute; left: 326px; top: 128px; width: 96px; height: 96px;
    border-radius: 50%; background: var(--badge); color: #fff;
    display: flex; flex-direction: column; align-items: center; justify-content: center;
    text-align: center; font-family: "Fira Sans Condensed", sans-serif; line-height: 1.15;
  }
  .offer-badge .head { font-weight: 700; font-size: 9.5px; }
  .offer-badge .small { font-size: 6px; font-weight: 500; }
  .offer-badge s { color: #7fc0e6; }
  .offer-badge .pay { font-weight: 700; font-size: 9px; }

  .step-bar {
    position: absolute; height: 15px; background: var(--brand-blue); color: #fff;
    font-family: "Fira Sans", Arial, sans-serif; font-weight: 500; font-size: 12px;
    display: flex; align-items: center; padding-left: 2px; line-height: 1;
  }
  .step-num {
    width: 17px; height: 17px; border-radius: 50%; background: #fff; color: var(--brand-blue);
    border: 1.5px solid var(--brand-blue);
    display: inline-flex; align-items: center; justify-content: center;
    font-size: 11px; margin-right: 9px; margin-left: -2px;
  }
  .options {
    position: absolute; display: grid; text-align: center;
    font-size: 8.5px; line-height: 11px; font-weight: 300; color: #222;
  }
  .options small { font-size: 5.5px; display: block; line-height: 11px; }
  .opt-price {
    display: block; margin-top: 6px; color: var(--brand-blue);
    font-family: "Fira Sans Condensed", sans-serif; font-weight: 700; font-size: 7.5px;
  }
  .choices {
    position: absolute; left: 32px; right: 34px;
    display: flex; justify-content: center; gap: 28px;
    font-size: 8.5px; font-weight: 300;
  }
  .list {
    position: absolute; font-size: 8px; line-height: 1.45; font-weight: 300; color: #222;
  }
  .list .opt-price { display: inline; margin: 0 0 0 3px; }
</style>
</head>
<body>

<section class="page cover">
  <div class="cover-band cover-band--left" role="img" aria-label="Blue Greek key pattern band"></div>
  <div class="cover-band cover-band--right" role="img" aria-label="Blue Greek key pattern band"></div>
  <h1 class="cover-name">MERAKI KITCHEN</h1>
</section>

<section class="page menu">
  <div class="menu-brand">MERAKI KITCHEN</div>
  <h2 class="menu-title">Souvlaki<br>Bar and Grill</h2>

  <div class="rule" style="top:105px"></div>
  <div class="photo photo--wrap" role="img" aria-label="Photo of a souvlaki pita wrap with fries"></div>
  <h3 class="item-title" style="top:115px">Souvliaki Pita Wrap <span class="price">£ 5.50</span></h3>
  <p class="intro">Get a whole meal all wrapped up with our delicious Greek Pita Wraps. Containing protein, sauce and salad</p>
  <div class="offer-badge">
    <span class="head">Buy two wraps<br>and save.<br>Takeaway only!</span>
    <span class="small">Double Souvlaki Pita Wrap Offer!</span>
    <span class="small">Instead of 2x5.5 = <s>£11</s></span>
    <span class="pay">pay £10.5!</span>
  </div>

  <div class="step-bar" style="left:32px;right:34px;top:206px"><span class="step-num">1</span>Choose Base:</div>
  <div class="options" style="left:32px;right:34px;top:229px;grid-template-columns:repeat(9,1fr)">
    <div>Chicken<br>Skewer<span class="opt-price">+ £ 0.50</span></div>
    <div>Pork<br>Skewer<span class="opt-price">+ £ 0.50</span></div>
    <div>Gyros<br>Chicken<span class="opt-price">+ £ 1.50</span></div>
    <div>Gyros<br>Pork<span class="opt-price">+ £ 1.50</span></div>
    <div>Mixed<br>Gyros<span class="opt-price">+ £ 2.00</span></div>
    <div>Kebab<small>(lamb + beef)</small><span class="opt-price">+ £ 0.50</span></div>
    <div>Haloumi<br>&nbsp;<span class="opt-price">+ £ 0.50</span></div>
    <div>Sausage<br>&nbsp;<span class="opt-price">+ £ 0.50</span></div>
    <div>No Base<br>&nbsp;<span class="opt-price">+ £ 0.50</span></div>
  </div>

  <div class="step-bar" style="left:32px;right:34px;top:272px"><span class="step-num">2</span>Add one of our delicious home made sauces:</div>
  <div class="choices" style="top:294px">
    <span>Tzatziki</span><span>Tyrokafteri</span><span>Burger Sauce</span><span>No Sauce</span>
  </div>

  <div class="step-bar" style="left:32px;right:34px;top:315px"><span class="step-num">3</span>Finalise it with the ingredients of your choice:</div>
  <div class="choices" style="top:335px">
    <span>Fries</span><span>Tomatoes</span><span>Onions</span><span>No Ingredients</span>
  </div>

  <div class="step-bar" style="left:32px;right:34px;top:358px"><span class="step-num">4</span>Feeling Hungry? Add extras:</div>
  <div class="options" style="left:38px;right:46px;top:379px;grid-template-columns:repeat(6,1fr)">
    <div>Double<br>Pita Bread<span class="opt-price">+ £ 1.00</span></div>
    <div>add Pork<br>Skewer<span class="opt-price">+ £ 2.50</span></div>
    <div>add Chicken<br>Skewer<span class="opt-price">+ £ 2.50</span></div>
    <div>add Kebab<br>(lamb+beef)<span class="opt-price">+ £ 2.50</span></div>
    <div>add<br>Sausage<span class="opt-price">+ £ 2.50</span></div>
    <div>add<br>Haloumi<span class="opt-price">+ £ 1.90</span></div>
  </div>

  <div class="rule" style="top:451px"></div>
  <div class="photo photo--platter" role="img" aria-label="Photo of a skewers platter with fries"></div>
  <h3 class="item-title item-title--platter" style="top:458px">Skewers and Gyros Platter <span class="price">£ 10.00</span></h3>

  <div class="step-bar" style="left:153px;right:34px;top:483px"><span class="step-num">1</span>Meat options:</div>
  <div class="list" style="left:156px;top:507px">2x Chicken Skewers<br>2x Pork Skewers<br>2x Kebab (lamb+beef)</div>
  <div class="list" style="left:280px;top:507px">3x Chicken Skewers<span class="opt-price">+ £ 3.00</span><br>3x Pork Skewers<span class="opt-price">+ £ 3.00</span><br>3x Kebab (lamb+beef)<span class="opt-price">+ £ 3.00</span></div>

  <div class="step-bar" style="left:32px;width:119px;top:551px"><span class="step-num">2</span>Choose Side:</div>
  <div class="step-bar" style="left:161px;width:119px;top:551px"><span class="step-num">3</span>Extras:</div>
  <div class="step-bar" style="left:297px;right:34px;top:551px"><span class="step-num">4</span>Pita Bread:</div>
  <div class="list" style="left:51px;top:574px">Fries<br>Side Salad<span class="opt-price">+ £ 2.50</span></div>
  <div class="list" style="left:178px;top:574px">Extra Haloumi<span class="opt-price">+ £ 3.50</span><br>Extra Tzatziki<span class="opt-price">+ £ 3.00</span></div>
  <div class="list" style="left:314px;top:574px">No Pita/1x Pita<br>2x Pita<span class="opt-price">+ £ 1.00</span></div>
</section>

</body>
</html>
```